FLOUR BAG DESIGN

• Bag dimensions: H=280 mm, A=105 mm, B=65 mm (look at the picture »dimensions«)
• Bag will be used for different types of flour (wheat flour, corn flour, buckwheat flour, etc.) and porridge (buckwheat, millet, etc. ) so we are looking for universal design that will suit to all of them. Please have in mind that somewhere on the front side (AxH) there needs to be some space for the name of the flour/porridge.
• I also uploaded design of an existing bag just in case you want to see it. Design on the bag represents the mill where our business started. We could say that existing bag is very traditional, we are looking for a little bit more modern style bag but still want to emphasize the link to our tradition.

I forgot to select "10 days " when desribing the label desing I need, before posting the project

• • We would like to integrate our logo (look at the picture »logo«) and text which is also present on the current bag. Front side AxH: Koleškov Mlin (name of the company), Fužina – Zagradec (name of the village), Meljemo že od 1682 (meaning Flour milling since 1682). On the right side: same as on the picture »current bag (dimensions BxH)«.

```html
<!DOCTYPE html>
<html lang="sl">
<head>
<meta charset="utf-8">
<title>Koleškov Mlin – Wheat Flour</title>
<link href="https://fonts.googleapis.com/css2?family=Arimo:ital,wght@0,400;0,700;1,400&display=swap" rel="stylesheet">
<style>
  :root {
    --brown: #6b3f1f;
    --brown-dark: #54301a;
    --tan: #a9876a;
    --cream: #f4e6cf;
    --sepia: #d9bf9a;
    --sun: #f8d65a;
    --paper: #ffffff;
  }
  html, body { margin: 0; padding: 0; overflow: hidden; background: var(--paper); }
  .bag-front {
    position: relative;
    width: 1200px;
    height: 3197px;
    overflow: hidden;
    background: var(--paper);
    font-family: "Arimo", Arial, sans-serif;
    color: var(--brown);
  }
  .brand-mark {
    position: absolute;
    top: 250px; left: 430px;
    width: 340px; height: 340px;
    border-radius: 50%;
    background: var(--brown);
  }
  .brand-name {
    position: absolute;
    top: 676px; left: 0; width: 100%;
    text-align: center;
    font-size: 138px;
    line-height: 1;
    font-weight: 400;
    color: var(--brown);
    margin: 0;
  }
  .product-ribbon {
    position: absolute;
    top: 1010px; left: 40px;
    width: 1120px; height: 210px;
  }
  .product-name {
    position: absolute;
    top: 1060px; left: 0; width: 100%;
    text-align: center;
    font-size: 92px;
    line-height: 1;
    font-weight: 700;
    color: var(--paper);
    margin: 0;
    letter-spacing: 2px;
  }
  .mill-illustration {
    position: absolute;
    top: 1225px; left: 100px;
    width: 1000px; height: 580px;
    background: radial-gradient(ellipse at 50% 45%, var(--cream) 0%, var(--sepia) 55%, #fff 100%);
  }
  .tagline {
    position: absolute;
    top: 1832px; left: 0; width: 100%;
    text-align: center;
    font-size: 92px;
    line-height: 1;
    font-weight: 400;
    margin: 0;
  }
  .footer-art {
    position: absolute;
    top: 2150px; left: 0;
    width: 1200px; height: 1047px;
  }
  .contact p {
    position: absolute;
    left: 0; width: 100%;
    margin: 0;
    text-align: center;
    line-height: 1;
    color: var(--brown-dark);
  }
  .contact .company { top: 2468px; font-size: 84px; font-weight: 700; }
  .contact .owner { top: 2562px; font-size: 56px; font-weight: 700; }
  .contact .address { top: 2634px; font-size: 52px; font-weight: 700; }
  .contact .phone-landline { top: 2836px; font-size: 49px; font-style: italic; }
  .contact .phone-mobile { top: 2906px; font-size: 49px; font-style: italic; }
  .contact .web { top: 3037px; font-size: 52px; font-style: italic; }
</style>
</head>
<body>
<main class="bag-front">
  <div class="brand-mark" aria-hidden="true"></div>
  <h1 class="brand-name">Koleškov mlin</h1>

  <svg class="product-ribbon" viewBox="0 0 1120 210" aria-hidden="true">
    <polygon points="0,65 130,65 130,195 0,195 55,130" fill="var(--brown-dark)"/>
    <polygon points="1120,65 990,65 990,195 1120,195 1065,130" fill="var(--brown-dark)"/>
    <path d="M80,20 Q560,-10 1040,20 L1040,160 Q560,130 80,160 Z" fill="var(--brown)"/>
  </svg>
  <h2 class="product-name">WHEAT FLOUR</h2>

  <div class="mill-illustration" role="img" aria-label="Sepia drawing of the old watermill buildings by the river"></div>

  <p class="tagline">Meljemo že od 1682</p>

  <svg class="footer-art" viewBox="0 0 1200 1047" aria-hidden="true">
    <defs>
      <radialGradient id="sunGlow" cx="600" cy="260" r="780" gradientUnits="userSpaceOnUse">
        <stop offset="0" stop-color="var(--sun)"/>
        <stop offset="0.45" stop-color="#fbe79f"/>
        <stop offset="1" stop-color="#ffffff" stop-opacity="0"/>
      </radialGradient>
    </defs>
    <path d="M0,230 Q600,330 1200,230 L1200,1047 L0,1047 Z" fill="url(#sunGlow)"/>
    <path d="M0,215 Q600,315 1200,215" fill="none" stroke="var(--brown)" stroke-width="26"/>
    <path d="M0,250 Q600,350 1200,250" fill="none" stroke="var(--tan)" stroke-width="12"/>
    <path d="M0,275 Q600,375 1200,275" fill="none" stroke="var(--brown)" stroke-width="6"/>
    <path d="M0,935 Q300,1010 600,965 Q900,920 1200,995" fill="none" stroke="var(--tan)" stroke-width="10"/>
    <path d="M0,965 Q300,1040 600,995 Q900,950 1200,1025 L1200,1047 L0,1047 Z" fill="var(--brown)"/>
  </svg>

  <section class="contact">
    <p class="company">Koleškov Mlin</p>
    <p class="owner">Janez Novak s.p.</p>
    <p class="address">Brezje 14, 1300 Dolina</p>
    <p class="phone-landline">T: 01 555 20 20</p>
    <p class="phone-mobile">M: 041 555 310</p>
    <p class="web">www.koleskov-mlin.si</p>
  </section>
</main>
</body>
</html>
```